NEW Modern Sleek Business Card for VR Language Startup

Our startup is using VR to lead the next wave of world language education. We need a two-sided business card that introduces the larger organization (Quorvel Language Inc) and our contact info on one side and shows the product, Lumidrasca, on the other side.

Side 1 (contact info)= Quorvel Logo and Contact info (name, title, phone, email)

Side 2 (product)= Lumidrasc logo, text, and website
Text= Culturally Immersive Language Learning Games
Website= www.lumidrasc.example

Target Market(s)

Education, Technology

Contact Information for Business Card

Contact info will be updated upon approval of the design. For now, put this as a placeholder.

Perry Hollins
Founder & CEO
phollins@mailtrove.example
(555)-014-2736

Font styles to use
Other font styles liked:
• Gibson and Century Gothic are the brand fonts

Requirements
Nice to have
• I would love to see cohesion between the design and colors of the two logos. I have attached a few business card designs that I like, so you can get a feel for my preferred style.

```html
<!DOCTYPE html>
<html lang="en">
<head>
<meta charset="utf-8">
<title>Quorvel Language – Business Card</title>
<link rel="stylesheet" href="https://fonts.googleapis.com/css2?family=Didact+Gothic&family=Lato:wght@400;700;900&display=swap">
<style>
  :root {
    --backdrop: #3a3b3e;
    --card-black: #050608;
    --card-white: #ffffff;
    --ink: #1b1b1b;
    --cyan: #3ec6ec;
    --violet: #6a5fcf;
    --name-red: #e8393a;
    --name-blue: #5a63c9;
    --icon-orange: #f0502c;
    --soft-white: #f2f2f2;
    --logo-grey: #9a9ca0;
  }
  * { box-sizing: border-box; margin: 0; padding: 0; }
  html, body { width: 1200px; height: 900px; overflow: hidden; }
  body {
    background: var(--backdrop);
    font-family: "Lato", sans-serif;
    position: relative;
  }
  .card {
    position: absolute;
    left: 250px;
    width: 700px;
    height: 400px;
    border-radius: 34px;
    overflow: hidden;
  }
  /* Product side */
  .card--product {
    top: 30px;
    background: var(--card-black);
    display: flex;
    flex-direction: column;
    align-items: center;
    justify-content: center;
    text-align: center;
  }
  .product-logo {
    display: flex;
    flex-direction: column;
    align-items: center;
    gap: 14px;
  }
  .product-logo__mark {
    width: 110px;
    height: 110px;
    border-radius: 50%;
    background: var(--cyan);
  }
  .product-logo__name {
    font-family: "Lato", sans-serif;
    font-weight: 700;
    font-size: 44px;
    color: var(--logo-grey);
    letter-spacing: 1px;
  }
  .product-tagline {
    margin-top: 18px;
    font-size: 21px;
    color: var(--cyan);
    letter-spacing: 0.3px;
  }
  .product-web {
    margin-top: 34px;
    display: flex;
    align-items: center;
    gap: 10px;
    font-size: 17px;
    color: var(--soft-white);
    letter-spacing: 0.5px;
  }
  .product-web svg { width: 12px; height: 12px; }

  /* Contact side */
  .card--contact {
    top: 470px;
    background: var(--card-white);
  }
  .contact-shape {
    position: absolute;
    inset: 0;
    width: 700px;
    height: 400px;
  }
  .contact-person {
    position: absolute;
    left: 44px;
    top: 44px;
  }
  .contact-person__name {
    font-weight: 900;
    font-size: 30px;
    line-height: 1.1;
  }
  .contact-person__first { color: var(--name-red); }
  .contact-person__last { color: var(--name-blue); }
  .contact-person__role {
    margin-top: 4px;
    font-size: 18px;
    color: var(--ink);
  }
  .contact-details {
    position: absolute;
    left: 64px;
    bottom: 36px;
    list-style: none;
    font-size: 19px;
    color: var(--ink);
  }
  .contact-details li {
    display: flex;
    align-items: center;
    gap: 12px;
    margin-top: 6px;
  }
  .contact-details svg { width: 18px; height: 18px; flex: none; }
  .company-logo {
    position: absolute;
    right: 52px;
    top: 92px;
    display: flex;
    flex-direction: column;
    align-items: center;
    gap: 22px;
    width: 280px;
  }
  .company-logo__mark {
    width: 100px;
    height: 100px;
    border-radius: 50%;
    background: var(--icon-orange);
  }
  .company-logo__name {
    font-family: "Didact Gothic", sans-serif;
    font-size: 30px;
    letter-spacing: 5px;
    color: var(--soft-white);
    text-transform: uppercase;
    text-align: center;
    line-height: 1.25;
  }
</style>
</head>
<body>

<section class="card card--product" aria-label="Product side">
  <div class="product-logo">
    <div class="product-logo__mark"></div>
    <div class="product-logo__name">Lumidrasc</div>
  </div>
  <p class="product-tagline">Culturally Immersive Language Learning Games</p>
  <p class="product-web">
    <svg viewBox="0 0 12 12" aria-hidden="true"><path d="M1 1 L11 5 L6.5 6.5 L5 11 Z" fill="#5aa0e8"/></svg>
    www.lumidrasc.example
  </p>
</section>

<section class="card card--contact" aria-label="Contact side">
  <svg class="contact-shape" viewBox="0 0 700 400" aria-hidden="true">
    <polygon points="260,0 700,0 700,400 430,400 260,250" fill="var(--card-black)"/>
    <polygon points="274,0 286,0 286,240 446,400 430,400 274,252" fill="var(--card-white)"/>
    <polygon points="300,0 700,0 700,400 470,400 300,236" fill="var(--card-black)"/>
  </svg>

  <div class="contact-person">
    <p class="contact-person__name"><span class="contact-person__first">Perry</span> <span class="contact-person__last">Hollins</span></p>
    <p class="contact-person__role">Founder &amp; CEO</p>
  </div>

  <ul class="contact-details">
    <li>
      <svg viewBox="0 0 24 24" aria-hidden="true"><path d="M6.6 10.8c1.4 2.8 3.8 5.1 6.6 6.6l2.2-2.2c.3-.3.7-.4 1-.2 1.1.4 2.3.6 3.6.6.6 0 1 .4 1 1V20c0 .6-.4 1-1 1C10.6 21 3 13.4 3 4c0-.6.4-1 1-1h3.5c.6 0 1 .4 1 1 0 1.3.2 2.5.6 3.6.1.3 0 .7-.2 1z" fill="var(--icon-orange)"/></svg>
      (555)-014-2736
    </li>
    <li>
      <svg viewBox="0 0 24 24" aria-hidden="true"><rect x="2" y="5" width="20" height="14" rx="1.5" fill="var(--icon-orange)"/><path d="M2.5 6 L12 13 L21.5 6" stroke="#fff" stroke-width="1.5" fill="none"/></svg>
      phollins@mailtrove.example
    </li>
  </ul>

  <div class="company-logo">
    <div class="company-logo__mark"></div>
    <div class="company-logo__name">Quorvel Language</div>
  </div>
</section>

</body>
</html>
```